Bright Harbor Charity - helping the disadvantaged

I would like a new web site design for my charity BRIGHT HARBOR. The charity provides help for the disadvantaged. See current site
brightharbor.org.au for details. Please refer to the current site for information on the charity. The objectives of the charity are in the "about us" tab. You will also notice on the site that we provide information about events that we sponsor an area for this should be provided on the site.

Target Market(s)

We have two targets:
1. Individuals and Businesses that will donate money to the charity.
2. Individuals that are in need of support from the charity.

Industry/Entity Type

Charity

Requirements
Must have
• Ability for individuals to be able to understand the type of support we can provide.
Nice to have
• Our logo should be prominate on each pages
Should not have
• Should be use modern fonts

```html
<!DOCTYPE html>
<html lang="en">
<head>
<meta charset="utf-8">
<title>Bright Harbor – Helping the Disadvantaged</title>
<link rel="stylesheet" href="https://fonts.googleapis.com/css2?family=Arimo:wght@400;700&family=Roboto+Condensed:wght@700&family=Fondamento&display=swap">
<style>
  :root{
    --page-bg:#ece5d2;
    --sheet:#ffffff;
    --green:#3d5234;
    --gold:#e0b22f;
    --gold-line:#ecc65a;
    --text:#6f7d63;
    --title:#5b6b4c;
    --border:#cfcfc8;
    --footer:#6a6a5e;
  }
  *{box-sizing:border-box;margin:0;padding:0}
  html,body{width:1200px;height:1067px;overflow:hidden}
  body{
    background:var(--page-bg);
    font-family:"Arimo",Arial,sans-serif;
    color:var(--text);
    position:relative;
  }
  .sheet{position:absolute;left:155px;top:0;width:903px;height:1003px;background:var(--sheet)}
  .abs{position:absolute}

  .brand{left:187px;top:32px;font-family:"Arimo",Arial,sans-serif;font-size:28px;font-weight:400;color:#5aa43b;letter-spacing:-.5px}
  .account{left:870px;top:53px;display:flex;gap:14px;font-family:"Arimo",Arial,sans-serif;font-size:14px;color:#222}
  .account span{display:flex;align-items:center;gap:6px}

  .nav{left:185px;top:90px;width:843px;height:41px;background:var(--gold);display:flex}
  .nav a{display:flex;align-items:center;justify-content:center;height:100%;
    font-family:"Roboto Condensed",Arial,sans-serif;font-weight:700;font-size:14.5px;color:#fff;text-decoration:none;
    border-right:1px solid var(--gold-line)}
  .nav a.current{background:var(--green);border-right:none}
  .nav a:last-child{border-right:none}

  .hero{left:185px;top:149px;width:843px;height:333px;
    background:linear-gradient(90deg,#b89a70 0%,#a3835a 30%,#6b5236 52%,#2a1c0d 70%,#1f1507 100%)}
  .hero p{position:absolute;left:446px;top:165px;font-family:"Fondamento",serif;font-size:28px;line-height:44px;color:#f1eadc}

  .card{border:1px solid var(--border);border-radius:6px;background:#fff;overflow:hidden}
  .card-head{height:43px;background:var(--green);display:flex;align-items:center;gap:6px;padding-left:18px;
    font-family:"Roboto Condensed",Arial,sans-serif;font-weight:700;font-size:24px;color:#fff;text-transform:uppercase}
  .card-body{font-size:12.4px;line-height:20.5px}
  .donate{left:185px;top:500px;width:248px;height:192px}
  .donate .card-body{padding:12px 14px 0;text-align:justify}
  .apply{left:451px;top:500px;width:279px;height:192px}
  .apply .card-body{padding:10px 14px 0 15px}
  .events{left:748px;top:500px;width:279px;height:456px}
  .events .card-body{padding:8px 10px 0 18px}
  .event{margin-bottom:22px}
  .event h3{font-size:12.4px;font-weight:700;color:var(--title);line-height:20.5px;margin-bottom:2px}
  .event p{text-align:justify}

  .about-title{left:199px;top:710px;font-family:"Roboto Condensed",Arial,sans-serif;font-weight:700;font-size:24px;color:var(--green)}
  .about-photo{left:203px;top:753px;width:145px;height:104px;background:radial-gradient(circle at 50% 55%,#a89f8f 0%,#c99a88 45%,#e4a695 75%,#8f8a6e 100%)}
  .about-text{font-size:12.4px;line-height:20.5px;text-align:justify}
  .about-text.first{left:359px;top:746px;width:374px}
  .about-text.second{left:203px;top:872px;width:527px}

  .footer{left:0;top:1027px;width:1200px;text-align:center;font-size:11.5px;color:var(--footer)}
</style>
</head>
<body>
  <div class="sheet"></div>

  <div class="abs brand">BRIGHT HARBOR</div>

  <div class="abs account">
    <span><svg width="11" height="14" viewBox="0 0 11 14"><rect x="0" y="6" width="11" height="8" rx="1" fill="#333"/><path d="M2.5 6V4a3 3 0 0 1 6 0v2" stroke="#333" stroke-width="1.8" fill="none"/></svg>Login</span>
    <span><svg width="16" height="14" viewBox="0 0 16 14"><circle cx="6" cy="4" r="3.2" fill="#333"/><path d="M0 14c0-4 2.7-6 6-6s6 2 6 6z" fill="#333"/><path d="M13 5v6M10 8h6" stroke="#333" stroke-width="1.6"/></svg>Register</span>
  </div>

  <nav class="abs nav">
    <a class="current" style="width:71px">HOME</a>
    <a style="width:109px">ABOUT US</a>
    <a style="width:88px">DONATE</a>
    <a style="width:73px">APPLY</a>
    <a style="width:88px">PLEDGE</a>
    <a style="width:101px">NOMINATE</a>
    <a style="width:87px">EVENTS</a>
    <a style="width:109px">CONTACT US</a>
    <a style="width:117px">DIRECTORS</a>
  </nav>

  <div class="abs hero" role="img" aria-label="Photo of cupped hands protecting a seedling growing in soil">
    <p>We need your support to<br>accommodate, feed and educate!</p>
  </div>

  <section class="abs card donate">
    <div class="card-head">
      <svg width="36" height="32" viewBox="0 0 36 32"><circle cx="11" cy="24" r="5" fill="none" stroke="#fff" stroke-width="2.5"/><path d="M6 10c6-6 16-6 22 2" stroke="#fff" stroke-width="3" fill="none"/><path d="M26 8l3 5-6 0z" fill="#fff"/></svg>
      Donate Now
    </div>
    <div class="card-body">Lorem Ipsum is simply dummy text of the printing and typesetting industry. Lorem Ipsum has been the industry's standard dummy text ever since the 1500s, when an unknown printer took a galley of type and scrambled it to make</div>
  </section>

  <section class="abs card apply">
    <div class="card-head">
      <svg width="32" height="36" viewBox="0 0 32 36"><path d="M16 20C6 12 6 4 11 3s5 3 5 4c0-1 1-5 5-4s5 9-5 17z" fill="#fff"/><path d="M2 26c5-2 9 2 14 2l10-4" stroke="#fff" stroke-width="3" fill="none"/></svg>
      Apply for a Help
    </div>
    <div class="card-body">Lorem Ipsum is simply dummy text of the printing and typesetting industry. Lorem Ipsum has been the industry's standard dummy text ever since the 1500s, when an unknown printer took a galley of type and scrambled it to make</div>
  </section>

  <section class="abs card events">
    <div class="card-head" style="padding-left:12px;gap:18px">
      <svg width="30" height="30" viewBox="0 0 30 30"><rect x="2" y="5" width="26" height="23" rx="2" fill="none" stroke="#fff" stroke-width="2.5"/><rect x="2" y="5" width="26" height="6" fill="#fff"/><path d="M8 2v6M22 2v6" stroke="#fff" stroke-width="2.5"/><path d="M8 14v11M13 14v11M18 14v11M23 14v11M6 17h19M6 22h19" stroke="#fff" stroke-width="1.5"/></svg>
      Latest Events
    </div>
    <div class="card-body">
      <article class="event"><h3>Harmony Day Information Sheet &amp;<br>Booking Form</h3><p>Tallowood's Inaugural Harmony Day Event 2012 Harmony Celebration Day – “EVERYONE BELONGS” Date: Saturday 24th March 2012</p></article>
      <article class="event"><h3>Harmony Day Information Sheet &amp;<br>Booking Form</h3><p>Tallowood's Inaugural Harmony Day Event 2012 Harmony Celebration Day – “EVERYONE BELONGS” Date: Saturday 24th March 2012</p></article>
      <article class="event"><h3>Harmony Day Information Sheet &amp;<br>Booking Form</h3><p>Tallowood's Inaugural Harmony Day Event 2012 Harmony Celebration Day – “EVERYONE BELONGS” Date: Saturday 24th March 2012</p></article>
    </div>
  </section>

  <h2 class="abs about-title">ABOUT US</h2>
  <div class="abs about-photo" role="img" aria-label="Photo of many hands arranged in a circle around a heap of sand"></div>
  <p class="abs about-text first">Lorem Ipsum is simply dummy text of the printing and typesetting industry. Lorem Ipsum has been the industry's standard dummy text ever since the 1500s, when an unknown printer took a galley of type and scrambled it to make a type specimen book. It has survived not only five centuries, but also the leap into electronic typesetting, remaining essentially unchanged.</p>
  <p class="abs about-text second">Lorem Ipsum is simply dummy text of the printing and typesetting industry. Lorem Ipsum has been the industry's standard dummy text ever since the 1500s, when an unknown printer took a galley of type and scrambled it to make a type specimen book. It has survived not only five centuries, but also the leap into electronic typesetting, remaining essentially unchanged. It</p>

  <footer class="abs footer">Copyright © 2012 Bright Harbor Proprietary Limited. All Rights Reserved.</footer>
</body>
</html>
```